Meridian Handsets business card design

I would like to see some designs for a business card for Meridian Handsets. I would like the business card to be double sided. It will need to have a similar colour / look and feel to our website www.meridianhandsets.com.au I have also attached our latest flyer. Final designs to be handed over in Photoshop format so that I can edit the business card when needed please.

Industry/Entity Type

Business

Contact Information for Business Card

Gavin Thornley
sales@meridianhandsets.com.au
Business Development Manager
ph: (08) 6197 5821
www.meridianhandsets.com.au

Font styles to use
Serif
Sans Serif

Requirements
Must have
• If you could please utilise our colour scheme as seen on our website and the attached flyer.
• I would also like the final design to be in a Photoshop format so that I can edit it when needed please.

```html
<!DOCTYPE html>
<html lang="en">
<head>
<meta charset="utf-8">
<title>Meridian Handsets – Business Card</title>
<link href="https://fonts.googleapis.com/css2?family=Fira+Sans:wght@400;600;700&display=swap" rel="stylesheet">
<style>
  :root {
    --bg: #eceae6;
    --card: #ffffff;
    --ink: #2f2f31;
    --brand-blue: #0a7cbf;
    --rule: #2f2f31;
  }
  * { margin: 0; padding: 0; box-sizing: border-box; }
  html, body {
    width: 1189px; height: 1200px; overflow: hidden;
    background: var(--bg);
    font-family: "Fira Sans", sans-serif;
    color: var(--ink);
  }
  .card {
    position: absolute;
    left: 171px; width: 856px; height: 488px;
    background: var(--card);
    box-shadow: 0 2px 6px rgba(0,0,0,0.18);
  }
  .card--front { top: 67px; }
  .card--back  { top: 627px; }

  .wordmark {
    position: absolute;
    font-weight: 600;
    font-size: 66px;
    letter-spacing: -0.5px;
    color: var(--ink);
    white-space: nowrap;
    line-height: 1;
  }
  .card--front .wordmark { left: 49px; top: 112px; }
  .card--back .wordmark { left: 0; right: 0; top: 218px; text-align: center; }

  .person {
    position: absolute; right: 42px; top: 272px; text-align: right;
  }
  .person__name {
    font-weight: 700; font-size: 32px; color: var(--brand-blue); line-height: 1.05;
  }
  .person__title {
    font-size: 22px; line-height: 1.2;
  }
  .rule {
    position: absolute; left: 43px; top: 316px; width: 426px; height: 2px;
    background: var(--rule);
  }
  .contacts {
    position: absolute; left: 43px; top: 358px; list-style: none;
    font-size: 22px; line-height: 32px;
  }
  .contacts li { display: flex; align-items: center; gap: 9px; }
  .contacts svg { width: 24px; height: 24px; flex: none; }
  .address {
    position: absolute; right: 42px; top: 362px; text-align: right;
    font-style: normal; font-size: 22px; line-height: 29px;
  }
</style>
</head>
<body>
  <section class="card card--front">
    <div class="wordmark">Meridian Handsets</div>

    <div class="person">
      <div class="person__name">Gavin Thornley</div>
      <div class="person__title">Business Development Manager</div>
    </div>
    <div class="rule"></div>

    <ul class="contacts">
      <li>
        <svg viewBox="0 0 24 24" aria-hidden="true">
          <rect width="24" height="24" fill="#0a7cbf"/>
          <path d="M8 4l3 4-2 2c1 2 3 4 5 5l2-2 4 3-2 3c-6 0-12-6-12-12z" fill="none" stroke="#fff" stroke-width="1.8" stroke-linejoin="round"/>
        </svg>
        <span>(08) 6197 5821</span>
      </li>
      <li>
        <svg viewBox="0 0 24 24" aria-hidden="true">
          <rect width="24" height="24" fill="#0a7cbf"/>
          <rect x="3" y="6" width="18" height="12" fill="none" stroke="#fff" stroke-width="1.6"/>
          <path d="M3 6l9 7 9-7M3 18l7-6M21 18l-7-6" fill="none" stroke="#fff" stroke-width="1.4"/>
        </svg>
        <span>sales@meridianhandsets.com.au</span>
      </li>
      <li>
        <svg viewBox="0 0 24 24" aria-hidden="true">
          <rect width="24" height="24" fill="#0a7cbf"/>
          <circle cx="12" cy="12" r="7.5" fill="none" stroke="#fff" stroke-width="1.6"/>
          <path d="M4.5 12h15M12 4.5c-3 3-3 12 0 15M12 4.5c3 3 3 12 0 15" fill="none" stroke="#fff" stroke-width="1.2"/>
        </svg>
        <span>www.meridianhandsets.com.au</span>
      </li>
    </ul>

    <address class="address">
      Kestrel Avenue<br>
      Ashgrove Park<br>
      Western Australia 6058
    </address>
  </section>

  <section class="card card--back">
    <div class="wordmark">Meridian Handsets</div>
  </section>
</body>
</html>
```